Female Pest Controller needs awesome business cards

I need a logo design for a Pest Control service - something that appeals to 'nature' & safe, with the use of the colour green. I am also female
New Business Name is 'Bug Begone Bay'
appeals to women

Target Market(s)

Domestic Households & Local Businesses

Industry/Entity Type

Pest Control

Contact Information for Business Card

Corinne Waldrake
0428316952
ABN 47 618 259 304
PMT7314958207
Spiders Cockroaches, Ants, Silverfish, Fleas, Rodents

Font styles to use
Decorative

Colors
abd036
aaaaaa
5c5c5c

Requirements
Should not have
• Pics of dead insects, prefer nature inspired designs, frogs, trees etc
• Have attached old log & business name ( now my ex's business) Lilyvale Pest Solutions -

```html
<!DOCTYPE html>
<html lang="en">
<head>
<meta charset="utf-8">
<title>Bug Begone Bay – Business Cards</title>
<link href="https://fonts.googleapis.com/css2?family=Montserrat:wght@400;500;700;800&display=swap" rel="stylesheet">
<style>
  :root {
    --backdrop: #e8e7e2;
    --card: #ffffff;
    --green: #7dbb35;
    --green-deep: #3f9a3b;
    --green-light: #abd036;
    --ink: #3d4a50;
    --grey: #5c5c5c;
    --grey-soft: #aaaaaa;
  }
  * { box-sizing: border-box; margin: 0; padding: 0; }
  html, body {
    width: 900px; height: 1200px; overflow: hidden;
    background: var(--backdrop);
    font-family: "Montserrat", Arial, sans-serif;
  }
  .card {
    position: absolute; left: 105px; width: 690px; height: 420px;
    background: var(--card); border-radius: 20px;
    box-shadow: 0 6px 18px rgba(0,0,0,.18);
    overflow: hidden;
  }
  .card--front { top: 120px; }
  .card--back { top: 640px; }

  .name-band {
    position: absolute; left: 0; top: 72px; width: 560px; height: 58px;
    background: linear-gradient(90deg, var(--green-deep) 0%, var(--green) 55%, rgba(171,208,54,.25) 85%, rgba(171,208,54,0) 100%);
    padding: 10px 0 0 36px;
    color: #fff; font-weight: 700; font-size: 31px; letter-spacing: .5px;
    text-transform: uppercase;
  }
  .job-title {
    position: absolute; left: 36px; top: 136px;
    background: var(--grey); color: #fff;
    font-size: 15px; font-weight: 500; letter-spacing: .5px;
    padding: 2px 14px 2px 0; margin-left: -36px; padding-left: 36px;
    text-transform: uppercase;
  }

  .mascot-art {
    position: absolute; border-radius: 40% 50% 45% 40%;
    background: radial-gradient(circle at 50% 45%, #8cc63f 0%, #5aa73c 45%, rgba(127,190,66,.35) 75%, rgba(255,255,255,0) 100%);
  }
  .card--front .mascot-art { left: 430px; top: 14px; width: 190px; height: 210px; }
  .card--back .mascot-art { left: 255px; top: 80px; width: 180px; height: 195px; }

  .brand { position: absolute; text-align: left; }
  .brand__name {
    font-weight: 800; font-size: 34px; color: var(--ink);
    text-transform: uppercase; letter-spacing: .5px; white-space: nowrap;
  }
  .brand__tag {
    font-weight: 500; font-size: 16px; color: var(--green);
    text-transform: uppercase; letter-spacing: 1px; margin-top: 2px;
  }
  .card--front .brand { left: 318px; top: 224px; }
  .card--back .brand { left: 0; right: 0; top: 290px; text-align: center; }

  .divider {
    position: absolute; left: 36px; right: 36px; top: 328px;
    border-top: 2px solid var(--grey-soft);
  }
  .contact { position: absolute; top: 344px; font-size: 16px; color: var(--grey); line-height: 25px; }
  .contact--left { left: 36px; }
  .contact--right { left: 372px; }
  .contact__row { display: flex; align-items: flex-start; gap: 10px; }
  .contact__row span.indent { padding-left: 30px; }
  .icon { width: 20px; height: 20px; flex: none; margin-top: 2px; }
</style>
</head>
<body>
  <section class="card card--front">
    <div class="name-band">Corinne Waldrake</div>
    <div class="job-title">Managing Director</div>

    <div class="mascot-art" role="img" aria-label="Illustration of a green tree frog climbing among leafy branches"></div>
    <div class="brand">
      <div class="brand__name">Bug Begone Bay</div>
      <div class="brand__tag">Pest Control Service</div>
    </div>

    <div class="divider"></div>

    <div class="contact contact--left">
      <div class="contact__row">
        <svg class="icon" viewBox="0 0 20 20"><circle cx="10" cy="10" r="10" fill="var(--green)"/><path d="M7 5.5l2 2-1.2 1.4a7 7 0 0 0 3.3 3.3l1.4-1.2 2 2-1.3 1.5C9.5 14 6 10.5 5.5 6.8z" fill="#fff"/></svg>
        <span>0428 316 952</span>
      </div>
      <div class="contact__row">
        <svg class="icon" viewBox="0 0 20 20"><circle cx="10" cy="10" r="10" fill="var(--green)"/><rect x="5" y="6.5" width="10" height="7" fill="#fff"/><path d="M5 6.5l5 4 5-4" fill="none" stroke="var(--green)" stroke-width="1.2"/></svg>
        <span>info@BugBegoneBay.com</span>
      </div>
    </div>

    <div class="contact contact--right">
      <div class="contact__row">
        <svg class="icon" viewBox="0 0 20 20"><circle cx="10" cy="10" r="10" fill="var(--green)"/><path d="M10 4.5a3.6 3.6 0 0 0-3.6 3.6c0 2.7 3.6 7.2 3.6 7.2s3.6-4.5 3.6-7.2A3.6 3.6 0 0 0 10 4.5z" fill="#fff"/><circle cx="10" cy="8.1" r="1.3" fill="var(--green)"/></svg>
        <span>3815 Fernbrook Avenue</span>
      </div>
      <div class="contact__row"><span class="indent">Suite 12, Bayview, CA 95062</span></div>
    </div>
  </section>

  <section class="card card--back">
    <div class="mascot-art" role="img" aria-label="Illustration of a green tree frog climbing among leafy branches"></div>
    <div class="brand">
      <div class="brand__name">Bug Begone Bay</div>
      <div class="brand__tag">Pest Control Service</div>
    </div>
  </section>
</body>
</html>
```